SOC audit and security advisory company

We are a small public accounting firm that specializes in SOC attestations for small to medium sized business throughout the U.S. Our business is much like consulting, but we form an opinion about their operational controls. We are looking for "relevance and with a hint of polished sophistication". Our logo colors are dark gray and red. Our existing site is www.veltrocheck.com for detailed information. We would like to include some type of captcha if possible. This is an information only site.

Target Market(s)

Small to medium sized financial and IT audit companies that are innovative and flexible.

Industry/Entity Type

Auditing

Coding

Coded - Design and coding required

Number of Pages Required

4 page

Font styles to use
Sans Serif

Requirements
Must have
• Good flow and attention to the content.
Nice to have
• CAPTCHA for contact us page
Should not have
• Big Bold lines.
• Too many distractions.

```html
<!DOCTYPE html>
<html lang="en">
<head>
<meta charset="utf-8">
<title>Contact Us – Veltro Check Audit &amp; Advisory</title>
<link href="https://fonts.googleapis.com/css2?family=Roboto:wght@400;500&family=Source+Sans+3:wght@400;600&display=swap" rel="stylesheet">
<style>
:root{
  --accent:#f15a22;
  --accent-soft:#f39a3c;
  --ink:#2f2f2f;
  --text:#555;
  --field:#efefef;
  --field-line:#cfcfcf;
  --footer:#e8e8e8;
  --rule:#cfcfcf;
  --white:#fff;
}
*{box-sizing:border-box;margin:0;padding:0}
html,body{width:987px;height:1200px;overflow:hidden;background:var(--white)}
body{position:relative;font-family:"Source Sans 3",sans-serif;color:var(--text)}
.abs{position:absolute}
.header{left:0;top:0;width:987px;height:89px;background:linear-gradient(90deg,#f3f3f1 0%,#e3e2de 35%,#f1f0ed 60%,#dcdad6 100%)}
.brand{display:flex;align-items:center;gap:6px;font-family:"Roboto",sans-serif;font-size:28px;font-weight:400;color:#555;letter-spacing:1px}
.brand-dot{width:10px;height:10px;border-radius:50%;background:var(--accent)}
.header .brand{left:65px;top:25px}
.nav a{position:absolute;top:35px;font-family:"Roboto",sans-serif;font-size:14px;color:var(--ink);text-decoration:none;white-space:nowrap}
.nav a.active{color:var(--accent)}
.btn-appoint{left:752px;top:21px;width:172px;height:43px;background:var(--accent);color:var(--white);font-family:"Roboto",sans-serif;font-size:14px;display:flex;align-items:center;justify-content:center}
.page-title{left:0;top:126px;width:987px;text-align:center;font-family:"Roboto",sans-serif;font-weight:400;font-size:34px;color:var(--ink)}
.page-title span{color:var(--accent)}
.intro{left:150px;top:175px;width:687px;text-align:center;font-size:12.5px;line-height:21px;color:var(--text)}
.map{left:0;top:255px;width:987px;height:296px;background:linear-gradient(90deg,#ebe7df 0%,#e9e6de 62%,#cfe3b8 66%,#cfe3b8 75%,#a9c8f5 78%,#a9c8f5 100%)}
.section-h{font-family:"Roboto",sans-serif;font-weight:400;font-size:26px;color:var(--ink)}
.info-list{left:65px;top:646px;font-size:12.5px;line-height:20.5px;color:var(--text)}
.info-row{display:flex;gap:9px;margin-bottom:6px}
.info-row svg{flex:none;margin-top:3px}
.info-row strong{font-weight:600;color:#444}
.socials{left:64px;top:815px;display:flex;gap:17px}
.social{width:43px;height:43px;border:1px solid var(--field-line);display:flex;align-items:center;justify-content:center}
.social.first{border-color:var(--accent)}
.social i{width:10px;height:10px;border-radius:50%;background:#555}
.social.first i{background:var(--accent)}
.divider{left:494px;top:581px;width:1px;height:231px;background:var(--rule)}
.field{background:var(--field);border:1px solid var(--field-line);font-size:12.5px;color:#888;padding:7px 12px}
.captcha{left:804px;top:808px;width:120px;height:30px;background:linear-gradient(90deg,#cfcfcf,#e4e4e4,#c9c9c9)}
.submit{left:512px;top:847px;width:129px;height:43px;border:1px solid var(--accent);color:var(--accent);font-family:"Roboto",sans-serif;font-size:19px;display:flex;align-items:center;justify-content:center}
.footer{left:0;top:936px;width:987px;height:264px;background:var(--footer)}
.foot-h{display:flex;align-items:center;gap:10px;font-family:"Roboto",sans-serif;font-size:19px;color:var(--accent-soft)}
.foot-text{font-size:12.5px;line-height:20.5px;color:var(--text)}
.foot-text a{color:var(--accent-soft);text-decoration:none}
.links li{list-style:none;margin-bottom:14px;font-size:13px;color:var(--text)}
.links li.hl{color:var(--accent-soft)}
.bottom-rule{left:64px;top:1159px;width:860px;height:1px;background:#888}
.copy{left:65px;top:1171px;font-size:12.5px;color:var(--text)}
.copy span{color:var(--accent-soft)}
.foot-social{left:826px;top:1172px;display:flex;gap:18px}
.foot-social i{width:11px;height:11px;border-radius:50%;background:#555}
.foot-social i:first-child{background:var(--accent-soft)}
</style>
</head>
<body>

<header class="abs header" role="img" aria-label="Soft-focus photo of a bright office interior behind the navigation">
  <div class="abs brand"><span class="brand-dot"></span>VELTRO</div>
  <nav class="nav">
    <a class="active" style="left:327px">Home</a>
    <a style="left:403px">About Us</a>
    <a style="left:499px">Services</a>
    <a style="left:590px">Contact Us</a>
  </nav>
  <div class="abs btn-appoint">MAKE APPOINTMENT</div>
</header>

<h1 class="abs page-title">CONTACT <span>US</span></h1>
<p class="abs intro">Thank you for your interest in Veltro Check services.&nbsp; We are glad you stopped by.&nbsp; For additional information regarding our audit and professional services offerings, please fill out the contact form and we will contact you promptly.</p>

<div class="abs map" role="img" aria-label="Street map showing the office location near the waterfront"></div>

<h2 class="abs section-h" style="left:65px;top:600px">CONTACT INFO</h2>
<div class="abs info-list">
  <div class="info-row">
    <svg width="13" height="17" viewBox="0 0 13 17"><path d="M6.5 1a5.5 5.5 0 0 0-5.5 5.5C1 10.5 6.5 16 6.5 16S12 10.5 12 6.5A5.5 5.5 0 0 0 6.5 1z" fill="var(--accent)"/><circle cx="6.5" cy="6.5" r="2" fill="#fff"/></svg>
    <div><strong>Veltro Check Audit &amp; Advisory, Inc</strong><br>410 Harbor Lane<br>Suite 212<br>Bayview, FL 33090<br>United States</div>
  </div>
  <div class="info-row">
    <svg width="17" height="16" viewBox="0 0 17 16"><path d="M3 1l3 3-2 2c1 2.5 3.5 5 6 6l2-2 3 3-2 2C7 14.5 2 9.5 1 3z" fill="var(--accent)"/></svg>
    <div>555 014 2290</div>
  </div>
  <div class="info-row">
    <svg width="17" height="13" viewBox="0 0 17 13"><rect x="1" y="1" width="15" height="11" fill="none" stroke="var(--accent)" stroke-width="1.5"/><path d="M1 1l7.5 6L16 1" fill="none" stroke="var(--accent)" stroke-width="1.5"/></svg>
    <div>info@veltrocheck.com</div>
  </div>
</div>
<div class="abs socials">
  <div class="social first" aria-label="Social profile"><i></i></div>
  <div class="social" aria-label="Social profile"><i></i></div>
  <div class="social" aria-label="Social profile"><i></i></div>
</div>

<div class="abs divider"></div>

<h2 class="abs section-h" style="left:540px;top:600px">GET IN TOUCH WITH US</h2>
<div class="abs field" style="left:512px;top:654px;width:198px;height:30px">Name</div>
<div class="abs field" style="left:727px;top:654px;width:197px;height:30px">Email</div>
<div class="abs field" style="left:512px;top:692px;width:198px;height:30px">Contact No.</div>
<div class="abs field" style="left:727px;top:692px;width:197px;height:30px">Company</div>
<div class="abs field" style="left:512px;top:731px;width:412px;height:69px">Message</div>
<div class="abs field" style="left:512px;top:808px;width:275px;height:30px">Verification Code</div>
<div class="abs captcha" role="img" aria-label="Distorted verification code image"></div>
<div class="abs submit">SUBMIT</div>

<footer class="abs footer">
  <div class="abs foot-h" style="left:65px;top:26px">
    <svg width="20" height="22" viewBox="0 0 20 22"><rect x="9" y="1" width="2.5" height="20" fill="var(--accent-soft)"/><rect x="1" y="4" width="17" height="3" fill="var(--accent-soft)"/><rect x="3" y="10" width="16" height="3" fill="var(--accent-soft)"/></svg>
    Company Information
  </div>
  <div class="abs brand" style="left:65px;top:82px"><span class="brand-dot"></span>VELTRO</div>
  <p class="abs foot-text" style="left:65px;top:154px;width:260px">Veltro Check was founded to put the consultation back into audit and professional services.</p>

  <div class="abs foot-h" style="left:358px;top:26px">
    <svg width="22" height="22" viewBox="0 0 22 22"><path d="M4 2l4 4-2.5 2.5c1.5 3 5 6.5 8 8L16 14l4 4-3 3C10 19.5 3 12 1.5 5z" fill="none" stroke="var(--accent-soft)" stroke-width="1.4"/></svg>
    Contact information
  </div>
  <div class="abs foot-text" style="left:358px;top:68px">Phone No. : <a>555 014 2290</a></div>
  <div class="abs foot-text" style="left:358px;top:102px">E-Mail Address :<br><a>info@veltrocheck.com</a></div>
  <div class="abs foot-text" style="left:358px;top:153px">Web Address :<br><a>&nbsp;www.veltrocheck.com</a></div>

  <div class="abs foot-h" style="left:651px;top:26px">
    <svg width="22" height="22" viewBox="0 0 22 22"><rect x="2" y="2" width="9" height="9" rx="3" fill="none" stroke="var(--accent-soft)" stroke-width="1.8" transform="rotate(45 6.5 6.5)"/><rect x="11" y="11" width="9" height="9" rx="3" fill="none" stroke="var(--accent-soft)" stroke-width="1.8" transform="rotate(45 15.5 15.5)"/></svg>
    Useful Links
  </div>
  <ul class="abs links" style="left:651px;top:68px">
    <li class="hl">&gt;&nbsp; Terms &amp; Conditions</li>
    <li>&gt;&nbsp; Disclaimer</li>
    <li>&gt;&nbsp; FAQ's</li>
  </ul>
</footer>
<div class="abs bottom-rule"></div>
<div class="abs copy">© <span>Veltro Check Audit &amp; Advisory, Inc.</span> - 2016 All rights reserved</div>
<div class="abs foot-social" aria-label="Social profiles"><i></i><i></i><i></i></div>

</body>
</html>
```